Business Card Design

The name of my business is called Amber Lantern, Inc.

We are the first brick and mortar store in our state that will specialize in spy equipment. I don't want the term "spy equipment" used in the design of the card. I would like a double sided card with the one side having all my contact information and the other side having the company name and the quote "Discreet Surveillance Equipment". I'm not looking for the perfect card on the first try but am not looking to make many changes.

I would like the card to speak sophistication so I tend to lean toward dark color backgrounds.

Industry/Entity Type

Store

Contact Information for Business Card

Gerald Moravec, Consultant
483-917-6052
gerald.moravec@amberlantern.net
www.amberlantern.net

```html
<!DOCTYPE html>
<html lang="en">
<head>
<meta charset="utf-8">
<title>Amber Lantern, Inc. — Business Card</title>
<link rel="stylesheet" href="https://fonts.googleapis.com/css2?family=Arimo:wght@400&display=swap">
<style>
  :root {
    --card-black: #000000;
    --type-blue: #1f4cf5;
    --swoosh-olive: #6e6d2c;
  }
  html, body {
    margin: 0;
    padding: 0;
    width: 1200px;
    height: 702px;
    overflow: hidden;
    background: var(--card-black);
  }
  .card {
    display: block;
    width: 1200px;
    height: 702px;
    background: var(--card-black);
    font-family: "Arimo", Arial, sans-serif;
  }
  .card-text { fill: var(--type-blue); font-family: "Arimo", Arial, sans-serif; }
  .company-name { font-size: 51px; }
  .tagline, .website, .job-title, .email, .phone { font-size: 24px; }
  .person-name { font-size: 38px; }
</style>
</head>
<body>
<svg class="card" viewBox="0 0 1200 702" xmlns="http://www.w3.org/2000/svg">
  <defs>
    <radialGradient id="burst-top-left" cx="0.35" cy="0.35" r="0.75">
      <stop offset="0" stop-color="#c8ff1a" stop-opacity="0.85"/>
      <stop offset="0.35" stop-color="#ff1fd0" stop-opacity="0.8"/>
      <stop offset="0.7" stop-color="#a25cff" stop-opacity="0.55"/>
      <stop offset="1" stop-color="#000000" stop-opacity="0"/>
    </radialGradient>
    <radialGradient id="burst-right" cx="0.55" cy="0.45" r="0.7">
      <stop offset="0" stop-color="#c8ff1a" stop-opacity="0.85"/>
      <stop offset="0.5" stop-color="#a25cff" stop-opacity="0.6"/>
      <stop offset="1" stop-color="#000000" stop-opacity="0"/>
    </radialGradient>
    <radialGradient id="swoosh-glow" cx="0.5" cy="0.5" r="0.5">
      <stop offset="0" stop-color="#6e6d2c" stop-opacity="0.45"/>
      <stop offset="1" stop-color="#000000" stop-opacity="0"/>
    </radialGradient>
  </defs>

  <rect class="burst burst-top-left" x="42" y="50" width="522" height="227" rx="110"
        fill="url(#burst-top-left)" role="img"
        aria-label="Cluster of bright concentric circles in pink, lime, violet and yellow"/>
  <rect class="burst burst-right" x="1051" y="299" width="96" height="337" rx="48"
        fill="url(#burst-right)" role="img"
        aria-label="Vertical cluster of lime, violet and yellow concentric circles with a curl"/>
  <rect class="swoosh-area" x="404" y="318" width="548" height="236" rx="118"
        fill="url(#swoosh-glow)" role="img"
        aria-label="Olive curved swoosh ornament sweeping across the card"/>

  <text class="card-text company-name" x="66" y="326">Amber Lantern, Inc.</text>
  <text class="card-text tagline" x="112" y="368">Discreet Surveillance Equipment</text>
  <text class="card-text website" x="156" y="414">www.amberlantern.net</text>

  <text class="card-text person-name" x="887" y="424" text-anchor="middle">Gerald Moravec</text>
  <text class="card-text job-title" x="888" y="462" text-anchor="middle">Consultant</text>
  <text class="card-text email" x="820" y="518" text-anchor="middle">gerald.moravec@amberlantern.net</text>
  <text class="card-text phone" x="938" y="578" text-anchor="middle">483-917-6052</text>
</svg>
</body>
</html>
```